Granite Ridge Response Business Card

Side 1: Granite Ridge Response Logo (logo without Maltese cross) with industrial rope rescue related theme. Our company services - TRAINING - Fire Training, Confined Space Rescue Training, Rope Rescue training, Hazmat Training, Incident Command, EMS, Pump Operations Training. Website - graniteridgeresponse.example.
Side 2: Granite Ridge Response Fire Department Logo (logo with Maltese cross) with Firefighter related theme. Company (division) services - FIELD SERVICES - Fire Department, Stand-by Rescue, Safety, EMS, Planning. "Supporting the Emergency Response Community Since 1967"

Add contact information wherever it makes since (Name, Email, Phone).
I would like it to represent the Granite Ridge Response Fire Department Logo as a division not as a separate entity without saying it, possibly by depicting it in the background of Side 2 instead of being a standalone picture like the logo on Side 1.

```html
<!DOCTYPE html>
<html lang="en">
<head>
<meta charset="utf-8">
<title>Granite Ridge Response Business Card</title>
<link rel="stylesheet" href="https://fonts.googleapis.com/css2?family=Arimo:wght@400;700&display=swap">
<style>
  :root {
    --page-bg: #dcdcdc;
    --card-bg: #ffffff;
    --ink: #111111;
    --ink-soft: #2a2a2a;
    --field-accent: #e8452c;
    --training-accent: #e2232a;
  }
  * { box-sizing: border-box; margin: 0; padding: 0; }
  html, body { width: 1051px; height: 1200px; overflow: hidden; }
  body {
    background: var(--page-bg);
    font-family: "Arimo", Arial, sans-serif;
    color: var(--ink);
    position: relative;
  }
  .card {
    position: absolute;
    left: 108px;
    width: 837px;
    height: 476px;
    background: var(--card-bg);
  }
  .card--field { top: 94px; }
  .card--training { top: 624px; }

  /* Field services side */
  .brand-mark {
    position: absolute;
    display: flex;
    align-items: center;
    gap: 12px;
    font-weight: 700;
    letter-spacing: 2px;
    white-space: nowrap;
  }
  .card--field .brand-mark {
    left: 0; right: 0; top: 150px;
    justify-content: center;
    font-size: 30px;
    color: var(--ink);
  }
  .brand-square { width: 22px; height: 22px; background: var(--field-accent); flex: none; }
  .tagline {
    position: absolute; left: 0; right: 0; top: 210px;
    text-align: center; font-size: 17px; color: var(--ink);
  }
  .contact-person {
    position: absolute; right: calc(837px - 297px); top: 278px; text-align: right;
  }
  .contact-person__name { font-size: 30px; line-height: 1.1; }
  .contact-person__role { font-size: 19px; color: var(--ink-soft); padding-right: 6px; }
  .contact-divider {
    position: absolute; left: 343px; top: 280px; width: 3px; height: 63px; background: var(--ink);
  }
  .contact-list { position: absolute; left: 396px; top: 283px; list-style: none; }
  .contact-list li {
    display: flex; align-items: center; gap: 15px;
    font-size: 24px; color: var(--ink-soft); height: 33px;
  }
  .contact-icon { width: 18px; height: 18px; flex: none; }
  .section-title {
    position: absolute; font-weight: 400; letter-spacing: 0.5px;
  }
  .card--field .section-title {
    left: 82px; top: 397px; font-size: 20px; color: var(--field-accent);
  }
  .service-row {
    position: absolute; left: 83px; top: 424px; list-style: none;
    display: flex; font-size: 18px; color: var(--ink-soft);
  }
  .service-row li { display: flex; align-items: center; gap: 7px; }
  .service-row li:nth-child(1) { width: 179px; }
  .service-row li:nth-child(2) { width: 200px; }
  .service-row li:nth-child(3) { width: 109px; }
  .service-row li:nth-child(4) { width: 96px; }
  .bullet { width: 10px; height: 10px; background: var(--field-accent); flex: none; }

  /* Training side */
  .card--training .brand-mark {
    left: 480px; width: 320px; top: 100px;
    flex-direction: column; gap: 4px;
    font-size: 32px; color: var(--training-accent); letter-spacing: 1px;
    line-height: 1.1; text-align: center;
  }
  .card--training .section-title {
    left: 50px; top: 150px; font-size: 30px; color: var(--training-accent); letter-spacing: 1px;
  }
  .training-list { position: absolute; left: 50px; top: 207px; list-style: none; }
  .training-list li {
    display: flex; align-items: center; gap: 10px;
    font-size: 22px; color: var(--ink-soft); height: 27px;
  }
  .training-list .bullet { background: var(--training-accent); }
  .web-line {
    position: absolute; left: 0; right: 0; top: 412px;
    display: flex; justify-content: center; align-items: center; gap: 10px;
    font-size: 24px; color: var(--ink);
  }
  .web-line__rule { width: 100px; height: 2px; background: var(--training-accent); }
</style>
</head>
<body>
  <section class="card card--field" aria-label="Field services side">
    <div class="brand-mark"><span class="brand-square"></span>GRANITE RIDGE RESPONSE</div>
    <p class="tagline">Supporting the Emergency Response Community Since 1967</p>

    <div class="contact-person">
      <div class="contact-person__name">Daniel Hartwell</div>
      <div class="contact-person__role">Director</div>
    </div>
    <div class="contact-divider"></div>
    <ul class="contact-list">
      <li>
        <svg class="contact-icon" viewBox="0 0 18 18" aria-hidden="true">
          <rect width="18" height="18" fill="#e8452c"/>
          <path d="M5 3.5h2.2l1 3-1.4 1a6 6 0 0 0 3.7 3.7l1-1.4 3 1V13a1.5 1.5 0 0 1-1.6 1.5A10 10 0 0 1 3.5 5.1 1.5 1.5 0 0 1 5 3.5z" fill="#fff"/>
        </svg>
        (555) 014 2290
      </li>
      <li>
        <svg class="contact-icon" viewBox="0 0 18 18" aria-hidden="true">
          <rect width="18" height="18" fill="#e8452c"/>
          <rect x="3.5" y="5" width="11" height="8" fill="none" stroke="#fff" stroke-width="1.2"/>
          <path d="M3.5 5.2 9 9.5l5.5-4.3" fill="none" stroke="#fff" stroke-width="1.2"/>
        </svg>
        info@graniteridgeresponse.example
      </li>
    </ul>

    <h2 class="section-title">FIELD SERVICES</h2>
    <ul class="service-row">
      <li><span class="bullet"></span>Fire Department</li>
      <li><span class="bullet"></span>Stand-by Rescue</li>
      <li><span class="bullet"></span>Safety</li>
      <li><span class="bullet"></span>EMS</li>
      <li><span class="bullet"></span>Planning</li>
    </ul>
  </section>

  <section class="card card--training" aria-label="Training side">
    <div class="brand-mark"><span>GRANITE RIDGE</span><span>RESPONSE</span></div>
    <h2 class="section-title">TRAINING</h2>
    <ul class="training-list">
      <li><span class="bullet"></span>Fire Training</li>
      <li><span class="bullet"></span>Confined Space Rescue Training</li>
      <li><span class="bullet"></span>Rope Rescue Training</li>
      <li><span class="bullet"></span>Hazmat Training</li>
      <li><span class="bullet"></span>Incident Command</li>
      <li><span class="bullet"></span>EMS</li>
      <li><span class="bullet"></span>Pump Operations Training</li>
    </ul>
    <div class="web-line">
      <span class="web-line__rule"></span>
      <span>www.graniteridgeresponse.example</span>
      <span class="web-line__rule"></span>
    </div>
  </section>
</body>
</html>
```